Plenvarique - product list page and product page - exclusive for TS

Regarding the homepage layout you made for the project Quilmarde - Plenvarique (ref 3192045) can you make the e-shop product list page and the product presentation page.
The product list page must diplay filter options (Manufacturer, category, Brand, Scale + keyword search) and display products as list with description and price.
The product presentation page must display product image in big, product details (Manufacturer, category, Brand, Scale, Year, price)
The website will be responsive and build with WordPress Woocommerce
1 page

```html
<!DOCTYPE html>
<html lang="en">
<head>
<meta charset="utf-8">
<title>Plenvarique – Product List</title>
<link href="https://fonts.googleapis.com/css2?family=Roboto:wght@400;500;700&family=Roboto+Condensed:wght@400;700&display=swap" rel="stylesheet">
<style>
:root{
  --teal:#3bb7b0;
  --nav-top:#62d2e2;
  --nav-bottom:#36a9c0;
  --nav-active:#5fcca0;
  --cart:#37b3c6;
  --price:#d9383a;
  --ink:#333;
  --muted:#666;
  --line:#d8d8d8;
  --topbar:#efefef;
  --footer:#8ecbb5;
  --footer-dark:#262626;
  --page-btn:#4a5560;
  --subscribe:#f25a5f;
}
*{box-sizing:border-box;margin:0;padding:0}
html,body{width:731px;height:1200px;overflow:hidden;background:#fff;font-family:"Roboto",sans-serif;color:var(--ink)}
.canvas{position:relative;width:731px;height:1200px}
.topbar{height:32px;background:var(--topbar);display:flex;align-items:center;justify-content:space-between;padding:0 53px;font-size:8px;color:#555}
.topbar .links span{margin:0 3px}
.lang{display:flex;align-items:center;gap:4px}
.lang i{width:9px;height:6px;background:#5a6fa8;display:inline-block}
.header{position:relative;height:80px}
.logo{position:absolute;left:55px;top:26px;font-family:"Roboto Condensed",sans-serif;font-size:25px;color:var(--teal);letter-spacing:0.3px}
.phone{position:absolute;left:360px;top:29px;display:flex;align-items:center;gap:10px;font-size:12px;color:#333}
.phone .ring{width:24px;height:24px;border:1px solid var(--teal);border-radius:50%;display:flex;align-items:center;justify-content:center}
.search{position:absolute;left:484px;top:30px;width:138px;height:23px;border:1px solid #ccc;display:flex}
.search span{flex:1;font-size:7px;color:#777;padding:8px 9px}
.search b{width:21px;background:var(--cart);display:flex;align-items:center;justify-content:center}
.basket{position:absolute;left:641px;top:27px;width:27px;height:27px;border:1px solid #333;border-radius:50%}
.basket em{position:absolute;right:-9px;top:-8px;width:15px;height:15px;border:1px solid #333;border-radius:50%;background:#fff;font-style:normal;font-size:9px;text-align:center;line-height:14px}
.nav{position:absolute;left:53px;top:112px;width:625px;height:38px;background:linear-gradient(var(--nav-top),var(--nav-bottom));display:flex;align-items:center;padding-left:4px;box-shadow:0 6px 8px -4px rgba(0,0,0,.25)}
.nav a{color:#fff;font-size:8px;text-decoration:none;padding:0 10px;height:38px;line-height:38px}
.nav a.active{background:var(--nav-active)}
.filters{position:absolute;left:53px;top:168px;width:625px;height:68px;background:#efefef;border:1px solid #ddd;box-shadow:0 2px 4px rgba(0,0,0,.2);display:flex;gap:11px;padding:11px 0 0 11px}
.filter label{display:block;font-size:8px;color:#333;margin-bottom:5px}
.filter .box{width:104px;height:25px;background:#fff;border:1px solid #ccc;font-size:7.5px;color:#444;display:flex;align-items:center;justify-content:space-between;padding:0 6px}
.filter .box i{border:3px solid transparent;border-top:3px solid #333;margin-top:3px}
.catalog{position:absolute;left:53px;top:250px;width:625px;height:740px;border:1px solid #ccc}
.catalog h2{position:absolute;left:19px;top:24px;font-family:"Roboto Condensed",sans-serif;font-weight:400;font-size:15px;color:var(--teal)}
.grid{position:absolute;left:11px;top:60px;display:grid;grid-template-columns:repeat(4,145px);column-gap:5.5px;row-gap:13px}
.card{width:145px;height:197px;background:#fff;box-shadow:0 1px 3px rgba(0,0,0,.2)}
.photo{height:124px}
.info{text-align:center;padding-top:11px;position:relative;height:73px}
.info h3{font-weight:400;font-size:8px;color:#333}
.info p{font-size:5.8px;color:#333;margin-top:9px}
.price{position:absolute;left:13px;top:50px;font-size:8px;color:var(--price)}
.add{position:absolute;right:10px;top:44px;width:23px;height:23px;border-radius:50%;background:var(--cart);display:flex;align-items:center;justify-content:center}
.pager{position:absolute;left:12px;top:696px;display:flex;gap:6px}
.pager span{height:15px;min-width:15px;padding:0 4px;background:var(--page-btn);color:#fff;font-size:7px;display:flex;align-items:center;justify-content:center}
.pager .wide{padding:0 8px}
.pager .current{background:var(--cart)}
.footer{position:absolute;left:0;top:1010px;width:731px;height:128px;background:var(--footer);color:#fff}
.col{position:absolute;top:26px}
.col h4{font-weight:400;font-size:9.5px;margin-bottom:15px}
.about p{font-size:6px;line-height:10.6px;text-align:justify;width:120px}
.tweet{display:flex;gap:8px}
.tweet .bird{width:20px;height:14px;background:#fff;border-radius:50%;margin-top:2px}
.tweet div{font-size:5.2px;line-height:8.6px;width:102px;color:#eaf6f1}
.tweet strong{font-size:6.5px;color:#fff;display:block;margin-bottom:2px}
.links li{list-style:none;font-size:6.5px;margin-bottom:7px}
.links li::before{content:"›";margin-right:6px}
.social li{list-style:none;font-size:6.5px;display:flex;align-items:center;gap:8px;margin-bottom:4px}
.social i{width:15px;height:15px;border-radius:50%;border:1px solid #fff;display:inline-block}
.social .s1{background:#3b5998}.social .s2{background:#2fa4d8}.social .s3{background:#d34836}
.news .mail{width:120px;height:22px;background:#fff;border:1px solid #ccc;font-size:6.5px;font-style:italic;color:#777;padding:7px 7px}
.news .btn{margin-top:9px;width:65px;height:19px;background:var(--subscribe);font-size:7px;display:flex;align-items:center;justify-content:center;border-radius:2px}
.bottom{position:absolute;left:0;top:1138px;width:731px;height:62px;background:var(--footer-dark);color:#fff}
.pay{position:absolute;left:53px;top:16px}
.pay b{font-size:9px;font-weight:700;display:block;margin-left:6px}
.cards{display:flex;gap:4px;margin-top:3px}
.cards i{width:17px;height:10px;background:#d8d8d8;display:block}
.copy{position:absolute;right:53px;top:28px;font-size:7.5px}
</style>
</head>
<body>
<div class="canvas">
  <div class="topbar">
    <div class="links">WISH LIST (0)<span>|</span>MY ACCOUNT<span>|</span>SHOPPING CART<span>|</span>CHECKOUT<span></span> €<span></span>£<span></span>$</div>
    <div class="lang"><i></i>English ⌄</div>
  </div>

  <header class="header">
    <div class="logo">PLENVARIQUE</div>
    <div class="phone">
      <span class="ring"><svg width="11" height="11" viewBox="0 0 24 24"><path d="M6.6 10.8a15 15 0 0 0 6.6 6.6l2.2-2.2c.3-.3.7-.4 1-.2 1.1.4 2.3.6 3.6.6.6 0 1 .4 1 1V20c0 .6-.4 1-1 1A17 17 0 0 1 3 4c0-.6.4-1 1-1h3.5c.6 0 1 .4 1 1 0 1.3.2 2.5.6 3.6.1.3 0 .7-.2 1z" fill="#3bb7b0"/></svg></span>
      248-555-0143
    </div>
    <div class="search"><span>Search</span><b><svg width="10" height="10" viewBox="0 0 24 24"><circle cx="10" cy="10" r="6" fill="none" stroke="#fff" stroke-width="3"/><path d="M14.5 14.5 21 21" stroke="#fff" stroke-width="3"/></svg></b></div>
    <div class="basket"><em>0</em></div>
  </header>

  <nav class="nav">
    <a>HOME</a><a class="active">MINIATURE</a><a>CONNECTIONS</a><a>EVENTS</a><a>WHO ARE WE</a><a>CONTACTS</a><a>COND. GENERAL SALES</a><a>SHIPPING COST</a><a>RETRACTION</a>
  </nav>

  <section class="filters">
    <div class="filter"><label>Manufacturer</label><div class="box">All manufacturer<i></i></div></div>
    <div class="filter"><label>Category</label><div class="box">All category<i></i></div></div>
    <div class="filter"><label>Mark</label><div class="box">All brand<i></i></div></div>
    <div class="filter"><label>Ladder</label><div class="box">All Scale<i></i></div></div>
    <div class="filter"><label>or keyword search</label><div class="box">search<svg width="8" height="8" viewBox="0 0 24 24"><circle cx="10" cy="10" r="6" fill="none" stroke="#333" stroke-width="3"/><path d="M14.5 14.5 21 21" stroke="#333" stroke-width="3"/></svg></div></div>
  </section>

  <main class="catalog">
    <h2>VARLENNE</h2>
    <div class="grid">
      <article class="card"><div class="photo" role="img" aria-label="Rally car model, green and navy livery" style="background:radial-gradient(circle,#6f8a3f 0 22%,#f1f1f1 50%,#e4e4e4)"></div><div class="info"><h3>PRODUCT NAME</h3><p>Description: Corsani Veltro 1000 gt Duplice</p><span class="price">Price: $19.95</span><span class="add"><svg width="11" height="10" viewBox="0 0 24 22"><path d="M1 2h4l3 11h11l3-8H7" fill="none" stroke="#fff" stroke-width="3"/><circle cx="10" cy="18" r="2" fill="#fff"/><circle cx="17" cy="18" r="2" fill="#fff"/></svg></span></div></article>
      <article class="card"><div class="photo" role="img" aria-label="Red sedan model" style="background:radial-gradient(circle,#b8232d 0 22%,#f1f1f1 50%,#e4e4e4)"></div><div class="info"><h3>PRODUCT NAME</h3><p>Description: Corsani Veltro 1000 gt Duplice</p><span class="price">Price: $19.95</span><span class="add"><svg width="11" height="10" viewBox="0 0 24 22"><path d="M1 2h4l3 11h11l3-8H7" fill="none" stroke="#fff" stroke-width="3"/><circle cx="10" cy="18" r="2" fill="#fff"/><circle cx="17" cy="18" r="2" fill="#fff"/></svg></span></div></article>
      <article class="card"><div class="photo" role="img" aria-label="Blue classic saloon model" style="background:radial-gradient(circle,#3f78c8 0 22%,#f1f1f1 50%,#e4e4e4)"></div><div class="info"><h3>PRODUCT NAME</h3><p>Description: Corsani Veltro 1000 gt Duplice</p><span class="price">Price: $19.95</span><span class="add"><svg width="11" height="10" viewBox="0 0 24 22"><path d="M1 2h4l3 11h11l3-8H7" fill="none" stroke="#fff" stroke-width="3"/><circle cx="10" cy="18" r="2" fill="#fff"/><circle cx="17" cy="18" r="2" fill="#fff"/></svg></span></div></article>
      <article class="card"><div class="photo" role="img" aria-label="Grey-green sedan model" style="background:radial-gradient(circle,#7f8c7d 0 22%,#f1f1f1 50%,#e4e4e4)"></div><div class="info"><h3>PRODUCT NAME</h3><p>Description: Corsani Veltro 1000 gt Duplice</p><span class="price">Price: $19.95</span><span class="add"><svg width="11" height="10" viewBox="0 0 24 22"><path d="M1 2h4l3 11h11l3-8H7" fill="none" stroke="#fff" stroke-width="3"/><circle cx="10" cy="18" r="2" fill="#fff"/><circle cx="17" cy="18" r="2" fill="#fff"/></svg></span></div></article>

      <article class="card"><div class="photo" role="img" aria-label="Red hatchback model" style="background:radial-gradient(circle,#c22a2a 0 22%,#f1f1f1 50%,#e4e4e4)"></div><div class="info"><h3>PRODUCT NAME</h3><p>Description: Corsani Veltro 1000 gt Duplice</p><span class="price">Price: $19.95</span><span class="add"><svg width="11" height="10" viewBox="0 0 24 22"><path d="M1 2h4l3 11h11l3-8H7" fill="none" stroke="#fff" stroke-width="3"/><circle cx="10" cy="18" r="2" fill="#fff"/><circle cx="17" cy="18" r="2" fill="#fff"/></svg></span></div></article>
      <article class="card"><div class="photo" role="img" aria-label="Silver estate car model" style="background:radial-gradient(circle,#a8a8a8 0 22%,#f1f1f1 50%,#e4e4e4)"></div><div class="info"><h3>PRODUCT NAME</h3><p>Description: Corsani Veltro 1000 gt Duplice</p><span class="price">Price: $19.95</span><span class="add"><svg width="11" height="10" viewBox="0 0 24 22"><path d="M1 2h4l3 11h11l3-8H7" fill="none" stroke="#fff" stroke-width="3"/><circle cx="10" cy="18" r="2" fill="#fff"/><circle cx="17" cy="18" r="2" fill="#fff"/></svg></span></div></article>
      <article class="card"><div class="photo" role="img" aria-label="Blue racing coupe model" style="background:radial-gradient(circle,#2b3f9e 0 22%,#f1f1f1 50%,#e4e4e4)"></div><div class="info"><h3>PRODUCT NAME</h3><p>Description: Corsani Veltro 1000 gt Duplice</p><span class="price">Price: $19.95</span><span class="add"><svg width="11" height="10" viewBox="0 0 24 22"><path d="M1 2h4l3 11h11l3-8H7" fill="none" stroke="#fff" stroke-width="3"/><circle cx="10" cy="18" r="2" fill="#fff"/><circle cx="17" cy="18" r="2" fill="#fff"/></svg></span></div></article>
      <article class="card"><div class="photo" role="img" aria-label="Dark endurance prototype model" style="background:radial-gradient(circle,#3a3d44 0 22%,#f1f1f1 50%,#e4e4e4)"></div><div class="info"><h3>PRODUCT NAME</h3><p>Description: Corsani Veltro 1000 gt Duplice</p><span class="price">Price: $19.95</span><span class="add"><svg width="11" height="10" viewBox="0 0 24 22"><path d="M1 2h4l3 11h11l3-8H7" fill="none" stroke="#fff" stroke-width="3"/><circle cx="10" cy="18" r="2" fill="#fff"/><circle cx="17" cy="18" r="2" fill="#fff"/></svg></span></div></article>

      <article class="card"><div class="photo" role="img" aria-label="Black estate car model" style="background:radial-gradient(circle,#2a2a2a 0 22%,#f1f1f1 50%,#e4e4e4)"></div><div class="info"><h3>PRODUCT NAME</h3><p>Description: Corsani Veltro 1000 gt Duplice</p><span class="price">Price: $19.95</span><span class="add"><svg width="11" height="10" viewBox="0 0 24 22"><path d="M1 2h4l3 11h11l3-8H7" fill="none" stroke="#fff" stroke-width="3"/><circle cx="10" cy="18" r="2" fill="#fff"/><circle cx="17" cy="18" r="2" fill="#fff"/></svg></span></div></article>
      <article class="card"><div class="photo" role="img" aria-label="Orange sports coupe model" style="background:radial-gradient(circle,#ef8a1c 0 22%,#f1f1f1 50%,#e4e4e4)"></div><div class="info"><h3>PRODUCT NAME</h3><p>Description: Corsani Veltro 1000 gt Duplice</p><span class="price">Price: $19.95</span><span class="add"><svg width="11" height="10" viewBox="0 0 24 22"><path d="M1 2h4l3 11h11l3-8H7" fill="none" stroke="#fff" stroke-width="3"/><circle cx="10" cy="18" r="2" fill="#fff"/><circle cx="17" cy="18" r="2" fill="#fff"/></svg></span></div></article>
      <article class="card"><div class="photo" role="img" aria-label="Black and white police car model" style="background:radial-gradient(circle,#555 0 22%,#f1f1f1 50%,#e4e4e4)"></div><div class="info"><h3>PRODUCT NAME</h3><p>Description: Corsani Veltro 1000 gt Duplice</p><span class="price">Price: $19.95</span><span class="add"><svg width="11" height="10" viewBox="0 0 24 22"><path d="M1 2h4l3 11h11l3-8H7" fill="none" stroke="#fff" stroke-width="3"/><circle cx="10" cy="18" r="2" fill="#fff"/><circle cx="17" cy="18" r="2" fill="#fff"/></svg></span></div></article>
      <article class="card"><div class="photo" role="img" aria-label="Pale silver coupe model" style="background:radial-gradient(circle,#c4cbc2 0 22%,#f1f1f1 50%,#e4e4e4)"></div><div class="info"><h3>PRODUCT NAME</h3><p>Description: Corsani Veltro 1000 gt Duplice</p><span class="price">Price: $19.95</span><span class="add"><svg width="11" height="10" viewBox="0 0 24 22"><path d="M1 2h4l3 11h11l3-8H7" fill="none" stroke="#fff" stroke-width="3"/><circle cx="10" cy="18" r="2" fill="#fff"/><circle cx="17" cy="18" r="2" fill="#fff"/></svg></span></div></article>
    </div>
    <div class="pager">
      <span class="wide">Prev</span><span class="current">1</span><span>2</span><span>3</span><span>4</span><span>5</span><span>6</span><span>…</span><span>22</span><span class="wide">Next</span>
    </div>
  </main>

  <footer class="footer">
    <div class="col about" style="left:54px"><h4>ABOUT US</h4><p>psum is simply dummy text of the printing and typesetting industry. Lorem Ipsum has been the industry's standard dummy text ever since the 1500s, when an unknown printer took a galley of type and scrambled it to make a type</p></div>
    <div class="col" style="left:210px"><h4>CHIRPLINE</h4><div class="tweet"><span class="bird"></span><div><strong>Civora Tweets 1</strong>Online and high-tech start-ups could account for 4% of Australia's GDP and 540,000 jobs by 2033<br><br>http://civora.example/4kq7</div></div></div>
    <div class="col links" style="left:365px"><h4>LINKS</h4><ul><li>Home</li><li>Our Team</li><li>Listings</li><li>Services</li></ul></div>
    <div class="col social" style="left:450px"><h4>CONNECT US</h4><ul><li><i class="s1"></i>Linkora</li><li><i class="s2"></i>Chirpline</li><li><i class="s3"></i>Gloopa</li></ul></div>
    <div class="col news" style="left:555px"><h4>NEWSLETTER</h4><div class="mail">Enter Your Mail Id</div><div class="btn">SUBSCRIBE</div></div>
  </footer>

  <div class="bottom">
    <div class="pay"><b>Paynora</b><div class="cards"><i></i><i></i><i></i><i></i><i></i></div></div>
    <div class="copy">Copyright © 2015  All Rights Reserved</div>
  </div>
</div>
</body>
</html>
```